BrightHarbor Flowchart Marketing Flyer

We are an MSP IT company. We have created a flowchart that we would like jazzed up to use in marketing new customers. The flowchart is a visual for prospective clients to see, in a simple way, what our process is. The flowchart should be 8.5"x11". We do not want the template of the flowchart altered (no boxes moved around) but would like something visually appealing and clean looking. Our office colors are lime green, royal blue, with accent colors of orange and purple. We would like the colors incorporated into the design. The design should be modern. This flyer is not going to be mass mailed. It will be handed to a prospective client in a face to face meeting.
Updates

I have uploaded our company logo to my brief in a couple of formats. One of the designers requested this. Great idea! I apologize for not providing it to begin with - it's my first time using this Website and the first time I have been assigned a project.

I was not able to view over the weekend as I did not have access to my work computer. Also need to review with the rest of management team on Thursday 6/28

Target Market(s)

Potential clients for an MSP IT company

Industry/Entity Type

It Company

Requirements
Must have
• The template itself we don't want changed. In other words we don't want the boxes moved around.
Nice to have
• Text, lines, shading and color of boxes can be changed. Not all colors mentioned in the brief need to be used. Would like it easy on the eye.

```html
<!DOCTYPE html>
<html lang="en">
<head>
<meta charset="utf-8">
<title>BrightHarbor Process Flyer</title>
<link rel="stylesheet" href="https://fonts.googleapis.com/css2?family=Oswald:wght@600&family=Rubik:wght@700&family=Ubuntu:wght@400;700&display=swap">
<style>
  :root {
    --lime: #a6ce3a;
    --lime-light: #bfd93c;
    --royal: #1460ad;
    --orange: #f26b24;
    --purple: #9c2b8f;
    --white: #ffffff;
    --tile: #fafafa;
    --ink: #333333;
    --icon-bg: #ececec;
  }
  html, body { margin: 0; padding: 0; width: 1200px; height: 1200px; overflow: hidden; background: var(--white); }
  .flyer { display: block; width: 1200px; height: 1200px; }
  .panel { fill: var(--lime); }
  .panel-glow { fill: var(--lime-light); }
  .banner { fill: var(--royal); }
  .banner-dots { fill: none; stroke: var(--white); stroke-width: 1.5; stroke-dasharray: 2 4; }
  .banner-title { font-family: "Oswald", sans-serif; font-weight: 600; font-size: 36px; fill: var(--white); letter-spacing: 1px; }
  .brand-name { font-family: "Rubik", sans-serif; font-weight: 700; font-size: 44px; fill: var(--royal); }
  .brand-dot { fill: var(--royal); }
  .tile { fill: var(--tile); }
  .step-tile { fill: var(--royal); }
  .step-ring { fill: none; stroke: var(--white); stroke-width: 4; }
  .step-num { font-family: "Ubuntu", sans-serif; font-size: 44px; fill: var(--white); text-anchor: middle; }
  .pointer { fill: var(--purple); }
  .pointer-light { fill: #d9ea9a; }
  .badge { fill: var(--white); stroke: var(--royal); stroke-width: 2.5; }
  .badge-num { font-family: "Ubuntu", sans-serif; font-size: 20px; fill: var(--royal); text-anchor: middle; }
  .heading { font-family: "Rubik", sans-serif; font-weight: 700; font-size: 22px; fill: var(--purple); letter-spacing: 0.5px; }
  .bullets { font-family: "Ubuntu", sans-serif; font-size: 16.5px; fill: var(--ink); }
  .petal-orange { fill: var(--orange); }
  .petal-blue { fill: var(--royal); }
  .petal-label { font-family: "Rubik", sans-serif; font-weight: 700; font-size: 21px; fill: var(--white); }
  .icon-disc { fill: var(--icon-bg); }
  .icon-orange { fill: var(--orange); }
  .icon-stroke { fill: none; stroke: var(--orange); stroke-width: 7; }
  .growth-bar { fill: var(--white); }
  .growth-arrow { fill: var(--orange); }
  .lens { fill: none; stroke: #f6e35c; stroke-width: 9; }
  .lens-handle { stroke: #f6e35c; stroke-width: 10; stroke-linecap: round; }
  .placeholder-board { fill: url(#boardTone); }
  .placeholder-idea { fill: url(#ideaTone); }
</style>
</head>
<body>
<svg class="flyer" viewBox="0 0 1500 1500" xmlns="http://www.w3.org/2000/svg">
  <defs>
    <linearGradient id="boardTone" x1="0" y1="0" x2="0" y2="1">
      <stop offset="0" stop-color="#14474f"/>
      <stop offset="1" stop-color="#e0a035"/>
    </linearGradient>
    <linearGradient id="ideaTone" x1="0" y1="0" x2="0" y2="1">
      <stop offset="0" stop-color="#f4e25a"/>
      <stop offset="1" stop-color="#3d8fa3"/>
    </linearGradient>
  </defs>

  <!-- background panel -->
  <rect class="panel" x="66" y="222" width="1367" height="1055"/>
  <path class="panel-glow" d="M932,222 H1433 V730 C1400,600 1300,560 1180,520 C1040,470 935,400 932,222 Z"/>

  <!-- title banner -->
  <polygon class="banner" points="328,222 842,222 842,312 585,290 328,312"/>
  <polyline class="banner-dots" points="336,226 336,302 585,281 834,302 834,226"/>
  <text class="banner-title" x="585" y="272" text-anchor="middle">BRIGHTHARBOR PROCESS</text>

  <!-- brand -->
  <circle class="brand-dot" cx="1120" cy="352" r="16"/>
  <text class="brand-name" x="1146" y="368">HarborTech</text>

  <!-- path tiles -->
  <g class="path">
    <rect class="tile" x="138" y="273" width="86" height="104"/>
    <polygon class="pointer-light" points="162,288 198,288 180,316"/>
    <rect class="tile" x="138" y="388" width="86" height="84"/>
    <rect class="step-tile" x="138" y="483" width="86" height="86"/>
    <circle class="step-ring" cx="181" cy="526" r="28"/>
    <text class="step-num" x="181" y="542">1</text>

    <path class="tile" d="M138,580 H224 A28,28 0 0 0 252,608 V694 A114,114 0 0 1 138,580 Z"/>
    <rect class="tile" x="263" y="608" width="86" height="86"/>
    <rect class="tile" x="361" y="608" width="86" height="86"/>
    <rect class="tile" x="459" y="608" width="86" height="86"/>
    <path class="step-tile" d="M557,608 A114,114 0 0 1 671,722 H585 A28,28 0 0 0 557,694 Z"/>
    <circle class="step-ring" cx="607" cy="673" r="28"/>
    <text class="step-num" x="607" y="689">2</text>

    <path class="tile" d="M585,737 H671 A114,114 0 0 1 557,851 V765 A28,28 0 0 0 585,737 Z"/>
    <rect class="tile" x="459" y="765" width="86" height="86"/>
    <path class="tile" d="M447,765 V851 A28,28 0 0 0 419,879 H333 A114,114 0 0 1 447,765 Z"/>
    <path class="step-tile" d="M333,895 H419 A28,28 0 0 0 447,923 V1010 A114,114 0 0 1 333,895 Z"/>
    <circle class="step-ring" cx="395" cy="945" r="28"/>
    <text class="step-num" x="395" y="961">3</text>

    <rect class="tile" x="461" y="923" width="86" height="87"/>
    <rect class="tile" x="559" y="923" width="86" height="87"/>
    <path class="tile" d="M657,923 A28,28 0 0 0 685,895 H771 A114,114 0 0 1 657,1010 Z"/>
    <path class="tile" d="M685,883 A114,114 0 0 1 800,769 V855 A28,28 0 0 0 772,883 Z"/>
    <rect class="step-tile" x="811" y="769" width="86" height="86"/>
    <circle class="step-ring" cx="854" cy="812" r="28"/>
    <text class="step-num" x="854" y="828">4</text>
  </g>

  <!-- step 1 -->
  <g class="icon-analytics">
    <circle class="lens" cx="438" cy="420" r="42"/>
    <line class="lens-handle" x1="468" y1="452" x2="480" y2="476"/>
    <rect x="413" y="412" width="8" height="36" fill="#f6e35c"/>
    <rect x="426" y="398" width="8" height="50" fill="#f15a29"/>
    <rect x="439" y="406" width="8" height="42" fill="#f7941d"/>
    <rect x="452" y="420" width="8" height="28" fill="#14474f"/>
  </g>
  <polygon class="pointer" points="242,545 262,535 262,555"/>
  <circle class="badge" cx="293" cy="545" r="14"/>
  <text class="badge-num" x="293" y="552">1</text>
  <text class="heading" x="334" y="515">ASSESS ALIGNMENT</text>
  <text class="bullets">
    <tspan x="334" y="541">• Review Technology Philosophy</tspan>
    <tspan x="334" y="562">• Share Proprietary Method</tspan>
    <tspan x="334" y="583">• Assess Organizational Fit</tspan>
  </text>

  <!-- step 2 -->
  <rect class="placeholder-board" x="693" y="385" width="155" height="170" rx="10" role="img" aria-label="Illustration of a presenter at a board with an audience of three"/>
  <polygon class="pointer" points="597,583 617,583 607,600"/>
  <circle class="badge" cx="655" cy="590" r="14"/>
  <text class="badge-num" x="655" y="597">2</text>
  <text class="heading" x="700" y="598">ON BOARDING</text>
  <text class="bullets">
    <tspan x="690" y="624">• Establish Expectations</tspan>
    <tspan x="690" y="645">• Service Provider Transition</tspan>
    <tspan x="690" y="666">• Cybersecurity Review</tspan>
    <tspan x="690" y="687">• Backup/Protection Strategy</tspan>
  </text>

  <!-- step 3 -->
  <ellipse cx="248" cy="1152" rx="88" ry="10" fill="#d9ea9a"/>
  <rect class="placeholder-idea" x="185" y="880" width="125" height="268" rx="14" role="img" aria-label="Illustration of a businessman holding up a glowing light bulb idea"/>
  <polygon class="pointer" points="367,1030 387,1030 377,1013"/>
  <circle class="badge" cx="375" cy="1062" r="14"/>
  <text class="badge-num" x="375" y="1069">3</text>
  <text class="heading" x="423" y="1071">30 DAY EVALUTION</text>
  <text class="bullets">
    <tspan x="413" y="1097">• Develop IT Playbook</tspan>
    <tspan x="413" y="1118">• Major Risk Identification</tspan>
    <tspan x="413" y="1139">• Observe &amp; Document Tenders</tspan>
    <tspan x="413" y="1160">• Standards Alignment Plan</tspan>
  </text>

  <!-- strategy cycle -->
  <g class="cycle">
    <path class="petal-orange" d="M925.1,802.1 A225,225 0 0 1 1142.1,585.1 L1147.0,725.1 A85,85 0 0 0 1065.1,807.0 Z"/>
    <path class="petal-blue" transform="rotate(90 1150 810)" d="M925.1,802.1 A225,225 0 0 1 1142.1,585.1 L1147.0,725.1 A85,85 0 0 0 1065.1,807.0 Z"/>
    <path class="petal-orange" transform="rotate(180 1150 810)" d="M925.1,802.1 A225,225 0 0 1 1142.1,585.1 L1147.0,725.1 A85,85 0 0 0 1065.1,807.0 Z"/>
    <path class="petal-blue" transform="rotate(270 1150 810)" d="M925.1,802.1 A225,225 0 0 1 1142.1,585.1 L1147.0,725.1 A85,85 0 0 0 1065.1,807.0 Z"/>

    <!-- growth -->
    <rect class="growth-bar" x="1100" y="832" width="12" height="28"/>
    <rect class="growth-bar" x="1118" y="826" width="12" height="34"/>
    <rect class="growth-bar" x="1136" y="816" width="12" height="44"/>
    <rect class="growth-bar" x="1154" y="804" width="12" height="56"/>
    <rect class="growth-bar" x="1172" y="788" width="12" height="72"/>
    <path class="growth-arrow" d="M1102,828 C1140,820 1160,800 1168,776 L1156,772 L1194,756 L1186,794 L1178,782 C1168,812 1140,830 1102,834 Z"/>

    <!-- standards -->
    <circle class="icon-disc" cx="1155" cy="651" r="52"/>
    <circle class="icon-orange" cx="1134" cy="630" r="9"/>
    <circle class="icon-orange" cx="1176" cy="630" r="9"/>
    <circle class="icon-orange" cx="1155" cy="664" r="9"/>
    <circle class="icon-stroke" cx="1155" cy="651" r="30" style="stroke-width:3"/>
    <text class="petal-label" x="987" y="686">Standards</text>
    <text class="petal-label" x="987" y="711">Alignment</text>

    <!-- budget -->
    <circle class="icon-disc" cx="1307" cy="810" r="52"/>
    <circle class="icon-orange" cx="1307" cy="820" r="22"/>
    <rect class="icon-orange" x="1298" y="784" width="18" height="14" rx="3"/>
    <text x="1307" y="829" text-anchor="middle" font-family="Rubik, sans-serif" font-weight="700" font-size="24" fill="#ffffff">$</text>
    <text class="petal-label" x="1232" y="738">Budget</text>

    <!-- strategy -->
    <circle class="icon-disc" cx="993" cy="805" r="52"/>
    <circle class="icon-stroke" cx="993" cy="805" r="30"/>
    <circle class="icon-stroke" cx="993" cy="805" r="15"/>
    <line x1="993" y1="805" x2="1036" y2="805" stroke="#f26b24" stroke-width="6"/>
    <text class="petal-label" x="991" y="892">Strategy</text>

    <!-- risk -->
    <circle class="icon-disc" cx="1148" cy="968" r="52"/>
    <path d="M1108,980 A40,40 0 0 1 1120,952 L1134,966 A20,20 0 0 0 1128,980 Z" fill="#c1272d"/>
    <path d="M1120,952 A40,40 0 0 1 1148,940 L1148,960 A20,20 0 0 0 1134,966 Z" fill="#f26b24"/>
    <path d="M1148,940 A40,40 0 0 1 1176,952 L1162,966 A20,20 0 0 0 1148,960 Z" fill="#f7c51e"/>
    <path d="M1176,952 A40,40 0 0 1 1188,980 L1168,980 A20,20 0 0 0 1162,966 Z" fill="#3fae49"/>
    <polygon points="1146,980 1150,980 1152,946" fill="#333333"/>
    <text class="petal-label" x="1236" y="913">Risk</text>
    <text class="petal-label" x="1197" y="939">Assessment</text>
  </g>

  <!-- step 4 -->
  <polygon class="pointer" points="927,1048 947,1048 937,1031"/>
  <circle class="badge" cx="937" cy="1084" r="14"/>
  <text class="badge-num" x="937" y="1091">4</text>
  <text class="heading" x="980" y="1093">ONGOING STRATEGIC PLAN &amp;</text>
  <text class="heading" x="980" y="1123">EXECUTION</text>
  <text class="bullets">
    <tspan x="980" y="1148">• Develop &amp; Execute Annual Strategic Plan</tspan>
    <tspan x="980" y="1169">• Risk Assessment, Ranking, Mitigation</tspan>
    <tspan x="980" y="1190">• Prioritize Investments</tspan>
    <tspan x="980" y="1211">• Develop 5 Years Budget</tspan>
    <tspan x="991" y="1232">Harbor Solution Standard Alignment</tspan>
  </text>
</svg>
</body>
</html>
```